Bright Path Therapies business cards and stationary

Need business cards and stationary designed to match previously made logo for for a new company based in Sydney NSW called 'Bright Path Therapies'.

We provide early intervention services and diagnostic assessment for children with disability and their families. I would like designs that are colourful and child friendly - possibly using feet/footprints/steps on a white background. The final design should communicate that we are family friendly, accepting and fun to work with.

Target Market(s)

Parents and Families
Teachers
Allied Health Professionals

Industry/Entity Type

Psychology

Contact Information for Business Card

Bright Path Therapies
www.brightpaththerapies.example
info@brightpaththerapies.example

Font styles to use
Sans Serif
Decorative
Script

Requirements
Must have
• Match the font and colour scheme of logo, along with footprint picture
Nice to have
• Clean and simple, while reflecting that I am working with families.
• Also- editable for when we make staff specific cards.

```html
<!DOCTYPE html>
<html lang="en">
<head>
<meta charset="utf-8">
<title>Bright Path Therapies – Business Card</title>
<link rel="stylesheet" href="https://fonts.googleapis.com/css2?family=Quicksand:wght@500;700&family=Raleway:wght@400;500&display=swap">
<style>
  :root {
    --page: #ecebe8;
    --card-white: #ffffff;
    --coral: #e4504a;
    --coral-light: #ef6a60;
    --coral-dark: #cf3d38;
    --sky: #22a0d6;
    --ink: #ffffff;
    --brand-blue: #2a9fd6;
  }
  * { box-sizing: border-box; margin: 0; padding: 0; }
  html, body {
    width: 1200px; height: 780px; overflow: hidden;
    background: var(--page);
  }
  .sheet {
    width: 1200px; height: 780px;
    display: flex; align-items: center; justify-content: center; gap: 50px;
  }
  .card {
    width: 525px; height: 300px; position: relative; overflow: hidden;
    border-radius: 3px;
    box-shadow: 0 10px 28px rgba(0,0,0,.18);
  }

  /* Front */
  .card-front { background: var(--card-white); display: flex; flex-direction: column; }
  .front-brand {
    flex: 0 0 168px; display: flex; align-items: center; gap: 20px;
    padding-left: 42px;
  }
  .brand-dot {
    width: 64px; height: 64px; border-radius: 50%; background: var(--coral);
    flex: none;
  }
  .brand-name {
    font-family: "Quicksand", sans-serif; font-weight: 700; color: var(--brand-blue);
    line-height: 1;
  }
  .brand-name .brand-main { display: block; font-size: 44px; letter-spacing: 1px; }
  .brand-name .brand-sub { display: block; font-size: 17px; letter-spacing: 7px; margin-top: 8px; text-transform: uppercase; }

  .staff-band {
    flex: 0 0 34px; background: var(--sky); color: var(--ink);
    display: flex; align-items: center; padding-left: 42px;
    font-family: "Raleway", sans-serif; font-size: 16px;
  }
  .staff-name { font-family: "Quicksand", sans-serif; font-weight: 700; letter-spacing: 1.5px; text-transform: uppercase; }
  .staff-sep { margin: 0 8px; opacity: .8; }

  .contact-panel {
    flex: 1; background: linear-gradient(160deg, var(--coral-light), var(--coral));
    padding: 14px 0 0 42px; display: flex; flex-direction: column; gap: 6px;
  }
  .contact-line {
    display: flex; align-items: center; gap: 10px;
    font-family: "Raleway", sans-serif; font-size: 15px; color: var(--ink);
  }
  .contact-icon { width: 17px; height: 17px; flex: none; }

  /* Back */
  .card-back {
    background: radial-gradient(circle at 40% 40%, var(--coral-light), var(--coral) 60%, var(--coral-dark));
    display: flex; flex-direction: column; align-items: center; justify-content: center;
    color: var(--ink);
  }
  .card-back .brand-name { color: var(--ink); text-align: left; }
  .back-email {
    font-family: "Raleway", sans-serif; font-size: 15px; margin-top: 26px;
  }
</style>
</head>
<body>
<main class="sheet">
  <section class="card card-front" aria-label="Business card front">
    <div class="front-brand">
      <span class="brand-dot" aria-hidden="true"></span>
      <p class="brand-name"><span class="brand-main">Bright Path</span><span class="brand-sub">Therapies</span></p>
    </div>
    <div class="staff-band">
      <span class="staff-name">Jordan Lee</span><span class="staff-sep">|</span><span class="staff-role">Manager</span>
    </div>
    <div class="contact-panel">
      <p class="contact-line">
        <svg class="contact-icon" viewBox="0 0 20 20" aria-hidden="true"><circle cx="10" cy="10" r="10" fill="#fff"/><path d="M6.5 5.5l2 0 .8 2.3-1.2 1a6 6 0 0 0 3.1 3.1l1-1.2 2.3.8v2a1 1 0 0 1-1 1A8.5 8.5 0 0 1 5.5 6.5a1 1 0 0 1 1-1z" fill="#e4504a"/></svg>
        (02) 5550 0142
      </p>
      <p class="contact-line">
        <svg class="contact-icon" viewBox="0 0 20 20" aria-hidden="true"><circle cx="10" cy="10" r="10" fill="#fff"/><rect x="5" y="6.5" width="10" height="7" rx="1" fill="#e4504a"/><path d="M5.5 7l4.5 3.5L14.5 7" stroke="#fff" stroke-width="1" fill="none"/></svg>
        info@brightpaththerapies.example
      </p>
      <p class="contact-line">
        <svg class="contact-icon" viewBox="0 0 20 20" aria-hidden="true"><circle cx="10" cy="10" r="10" fill="#fff"/><g stroke="#e4504a" stroke-width="1.1" fill="none"><circle cx="10" cy="10" r="5"/><ellipse cx="10" cy="10" rx="2.2" ry="5"/><path d="M5 10h10"/></g></svg>
        www.brightpaththerapies.example
      </p>
    </div>
  </section>

  <section class="card card-back" aria-label="Business card back">
    <p class="brand-name"><span class="brand-main">Bright Path</span><span class="brand-sub">Therapies</span></p>
    <p class="back-email">info@brightpaththerapies.example</p>
  </section>
</main>
</body>
</html>
```